Road Construction Company needs business cards

We would like a new business card designed for our business.

We're a road construction company based in Qld, Australia.

Can the business card please have the following information on it.

Name: Brent Malvoy
Position: General Manager
Phone: 0471 592 304
Email: Brent.malvoy@quendix.com.au
Address: 87 Harrowgate Ave, Pindarra, QLD, 4000
Website: www.quendix.com.au

Visually we'd like the card to be professional and simple.

Attached is our logo.

Our website is www.quendix.com.au

Target Market(s)

Men aged 25-60

Contact Information for Business Card

As listed in project description

Font styles to use
Serif

Requirements
Must have
• Large logo on back of card

```html
<!DOCTYPE html>
<html lang="en">
<head>
<meta charset="utf-8">
<title>Quendix Business Card</title>
<link rel="stylesheet" href="https://fonts.googleapis.com/css2?family=Figtree:wght@400;600;800&display=swap">
<style>
  :root {
    --page-bg: #e6e6e4;
    --card-deep: #063a86;
    --card-mid: #0a4c9c;
    --card-light: #1667ad;
    --emboss: #0b468f;
    --ink: #ffffff;
    --ink-soft: #e4ecf7;
  }
  * { box-sizing: border-box; margin: 0; padding: 0; }
  html, body {
    width: 1200px;
    height: 1200px;
    overflow: hidden;
    background: var(--page-bg);
    font-family: "Figtree", Arial, sans-serif;
  }
  .canvas {
    position: relative;
    width: 1200px;
    height: 1200px;
  }
  .card {
    position: absolute;
    left: 234px;
    width: 731px;
    height: 418px;
    background: linear-gradient(225deg, var(--card-light) 0%, var(--card-mid) 50%, var(--card-deep) 100%);
    color: var(--ink);
  }
  .card--front { top: 160px; }
  .card--back { top: 632px; }

  .front-brand {
    position: absolute;
    left: 0;
    right: 0;
    top: 168px;
    text-align: center;
    font-weight: 800;
    font-size: 62px;
    letter-spacing: 4px;
    text-transform: uppercase;
    color: var(--emboss);
  }

  .contact {
    position: absolute;
    left: 63px;
    top: 58px;
  }
  .contact__name {
    font-weight: 600;
    font-size: 30px;
    line-height: 1.1;
  }
  .contact__role {
    margin-top: 8px;
    font-size: 19px;
    color: var(--ink-soft);
  }
  .contact__address {
    margin-top: 20px;
    font-size: 19px;
    line-height: 28px;
    color: var(--ink-soft);
  }
  .contact__list {
    list-style: none;
    margin-top: 16px;
    font-size: 19px;
    line-height: 27px;
    color: var(--ink-soft);
  }
  .contact__list li {
    display: flex;
    align-items: center;
    gap: 9px;
  }
  .contact__list svg {
    width: 16px;
    height: 16px;
    flex: none;
  }

  .back-brand {
    position: absolute;
    right: 65px;
    top: 308px;
    font-weight: 800;
    font-size: 42px;
    letter-spacing: 3px;
    text-transform: uppercase;
    color: var(--ink);
  }
</style>
</head>
<body>
<div class="canvas">
  <section class="card card--front">
    <div class="front-brand">Quendix</div>
  </section>

  <section class="card card--back">
    <div class="contact">
      <h1 class="contact__name">Brent Malvoy</h1>
      <p class="contact__role">General Manager</p>
      <p class="contact__address">87 Harrowgate Ave, Pindarra,<br>QLD, 4000</p>
      <ul class="contact__list">
        <li>
          <svg viewBox="0 0 16 16" aria-hidden="true"><path fill="#fff" d="M3.6 1.5l2.2 2.6-1.2 1.6c.9 2 2.6 3.7 4.6 4.6l1.6-1.2 2.6 2.2-1.3 2.2C6.8 13.3 2.7 9.2 1.4 3z"/></svg>
          0471 592 304
        </li>
        <li>
          <svg viewBox="0 0 16 16" aria-hidden="true"><rect x="1" y="3" width="14" height="10" rx="1" fill="#fff"/><path d="M1.5 3.8L8 9l6.5-5.2" fill="none" stroke="#0a4c9c" stroke-width="1.4"/></svg>
          Brent.malvoy@quendix.com.au
        </li>
        <li>
          <svg viewBox="0 0 16 16" aria-hidden="true"><g fill="none" stroke="#fff" stroke-width="1.4"><circle cx="8" cy="8" r="6.5"/><ellipse cx="8" cy="8" rx="2.8" ry="6.5"/><path d="M1.5 8h13"/></g></svg>
          www.quendix.com.au
        </li>
      </ul>
    </div>
    <div class="back-brand">Quendix</div>
  </section>
</div>
</body>
</html>
```